'Cradle Ahead' promotional brochure

We have designed a 6 week program to educate impending first-time parents about the things they need to know to survive the first 6 months. Sessions delivered by general practitioner/family doctor, dietician, physiotherapist, speech pathologist and psychologist. Our promotional blurb is: 'A comprehensive education program for first-time parents-to-be, delivered over 6 weeks by health professionals in your community, about everything you need to know to look after your baby (and yourself!) in the first 6 months'. I now want to put together a promotional brochure to be distributed to those couples who express an interest which will provide further details of what will be delivered in the course.
Updates
In terms of layout, I envisaged a double sided A4 size, foldable into 3 sections, but very happy to be guided on this.
Target Market(s)
To appeal to a young, well educated demographic. First time parents couples.
Industry/Entity Type
Medical
Font styles to use
Other font styles liked:
- Playfair Display
Requirements
Must have
- Playfair display font to be consistent with our logo (attached). Logo also included please. Some consistency with colours of logo please.
Nice to have
- I am a doctor, and have no creative genes! But prefer a clean and professional appearance overall. Not too cluttered in overall appearance.
Should not have
- No cheesy pictures of babies.

```html
<!DOCTYPE html>
<html lang="en">
<head>
<meta charset="utf-8">
<title>Cradle Ahead – Brochure Cover</title>
<link rel="stylesheet" href="https://fonts.googleapis.com/css2?family=Playfair+Display:wght@400;700&display=swap">
<style>
  :root {
    --backdrop: #f3f3f3;
    --panel-grey: #e4e4e4;
    --panel-grey-light: #eeeeee;
    --band-white: #f7f7f7;
    --brand-green: #6fbe1f;
    --brand-green-dark: #5aa312;
    --brand-green-light: #86d12e;
    --ink-grey: #4a4a4a;
    --photo-dark: #1a1a1a;
    --photo-mid: #6b6b6b;
    --photo-light: #b9b9b9;
    --frame-white: #ffffff;
  }

  * { margin: 0; padding: 0; box-sizing: border-box; }

  html, body {
    width: 1200px;
    height: 801px;
    overflow: hidden;
    background: var(--backdrop);
  }

  .brochure-cover {
    position: absolute;
    left: 430px;
    top: 40px;
    width: 340px;
    height: 720px;
    overflow: hidden;
    box-shadow: 0 6px 24px rgba(0, 0, 0, 0.12);
  }

  .cover-background {
    position: absolute;
    inset: 0;
  }

  .brand-lockup {
    position: absolute;
    left: 34px;
    top: 42px;
    display: flex;
    align-items: center;
    gap: 14px;
  }

  .brand-dot {
    width: 40px;
    height: 40px;
    border-radius: 50%;
    background: var(--brand-green);
    flex-shrink: 0;
  }

  .brand-name {
    font-family: "Playfair Display", serif;
    font-weight: 400;
    font-size: 19px;
    line-height: 1.05;
    letter-spacing: 0.5px;
    text-transform: uppercase;
    color: var(--ink-grey);
  }

  .hero-frame {
    position: absolute;
    left: 55px;
    top: 150px;
    width: 248px;
    height: 470px;
    background: var(--frame-white);
    padding: 5px;
  }

  .hero-photo {
    position: relative;
    width: 100%;
    height: 100%;
    background:
      radial-gradient(ellipse at 55% 30%, var(--photo-light) 0%, var(--photo-mid) 40%, transparent 75%),
      linear-gradient(180deg, #2a2a2a 0%, var(--photo-mid) 45%, var(--photo-dark) 100%);
  }

  .program-title {
    position: absolute;
    left: 18px;
    bottom: 16px;
    font-family: "Playfair Display", serif;
    font-weight: 400;
    color: var(--frame-white);
    text-transform: uppercase;
    line-height: 0.95;
  }

  .program-title .title-first {
    display: block;
    font-size: 38px;
    letter-spacing: 0.5px;
  }

  .program-title .title-second {
    display: block;
    font-size: 56px;
    letter-spacing: 1px;
  }
</style>
</head>
<body>
  <section class="brochure-cover">
    <svg class="cover-background" width="340" height="720" viewBox="0 0 340 720" aria-hidden="true">
      <defs>
        <linearGradient id="greyFade" x1="0" y1="0" x2="0" y2="1">
          <stop offset="0" stop-color="var(--panel-grey-light)"/>
          <stop offset="1" stop-color="var(--panel-grey)"/>
        </linearGradient>
      </defs>
      <rect class="grey-field" x="0" y="0" width="340" height="720" fill="url(#greyFade)"/>
      <polygon class="white-band" points="0,372 340,356 340,382 0,398" fill="var(--band-white)"/>
      <polygon class="green-field" points="0,398 340,382 340,720 0,720" fill="var(--brand-green)"/>
      <polygon class="green-fold" points="0,720 340,600 340,720" fill="var(--brand-green-dark)"/>
      <polygon class="green-sheen" points="120,720 340,640 340,720" fill="var(--brand-green-light)" opacity="0.6"/>
      <polygon class="accent-triangle" points="248,150 300,118 300,150" fill="var(--brand-green)"/>
    </svg>

    <div class="brand-lockup">
      <span class="brand-dot"></span>
      <p class="brand-name">Banksia<br>Family<br>Clinic</p>
    </div>

    <div class="hero-frame">
      <div class="hero-photo" role="img" aria-label="Black and white photograph of a mother and father holding their newborn baby close">
        <h1 class="program-title">
          <span class="title-first">Cradle</span>
          <span class="title-second">Ahead</span>
        </h1>
      </div>
    </div>
  </section>
</body>
</html>
```